Cover for Inspirational Daily Journal

This is the cover for a daily journal that will focus on inspirational content for black women. The cover should have a picture or silhouette of a black woman with a crown. The title is: "Grace in Bloom: A Year of Bright Mornings." The back won't have any words. Also the journal will be published on Pagewick.

```html
<!DOCTYPE html>
<html lang="en">
<head>
<meta charset="utf-8">
<title>Grace in Bloom: A Year of Bright Mornings — Cover</title>
<link rel="stylesheet" href="https://fonts.googleapis.com/css2?family=Bebas+Neue&display=swap">
<style>
  :root {
    --backdrop: #babdc7;
    --cover-black: #121216;
    --gold-deep: #b8901c;
    --gold-mid: #d9b64a;
    --gold-light: #e8cc63;
    --silver: #f2f0ec;
    --white: #ffffff;
    --portrait-light: #f4f4f4;
    --portrait-shade: #d6d6d8;
  }
  * { margin: 0; padding: 0; box-sizing: border-box; }
  html, body {
    width: 1200px;
    height: 791px;
    overflow: hidden;
    background: var(--backdrop);
  }
  .canvas {
    position: relative;
    width: 1200px;
    height: 791px;
  }
  .cover {
    position: absolute;
    left: 385px;
    top: 32px;
    width: 430px;
    height: 727px;
    background: var(--cover-black);
    overflow: hidden;
    font-family: "Bebas Neue", "Oswald", sans-serif;
  }
  .title {
    position: absolute;
    left: 40px;
    top: 70px;
    font-size: 164px;
    line-height: 146px;
    font-weight: 400;
    text-transform: uppercase;
    background: linear-gradient(135deg,
      var(--gold-deep) 0%,
      var(--gold-light) 22%,
      var(--gold-mid) 38%,
      var(--silver) 50%,
      var(--gold-mid) 60%,
      var(--gold-deep) 72%,
      var(--gold-light) 86%,
      var(--silver) 100%);
    -webkit-background-clip: text;
    background-clip: text;
    color: transparent;
  }
  .title span { display: block; }
  .subtitle {
    position: absolute;
    left: 42px;
    top: 580px;
    width: 232px;
    color: var(--white);
    text-transform: uppercase;
    font-weight: 400;
  }
  .subtitle .lead {
    display: block;
    font-size: 34px;
    line-height: 34px;
  }
  .subtitle .main {
    display: block;
    font-size: 38px;
    line-height: 40px;
    white-space: nowrap;
  }
  .portrait {
    position: absolute;
    left: 292px;
    top: 556px;
    width: 118px;
    height: 171px;
    border-radius: 59px 59px 10px 10px;
    background: radial-gradient(circle at 50% 40%, var(--portrait-light) 0%, var(--portrait-shade) 100%);
  }
</style>
</head>
<body>
  <main class="canvas">
    <section class="cover">
      <h1 class="title">
        <span>Grace</span>
        <span>In</span>
        <span>Bloom</span>
      </h1>
      <p class="subtitle">
        <span class="lead">A Year of</span>
        <span class="main">Bright Mornings</span>
      </p>
      <div class="portrait" role="img" aria-label="White silhouette of a Black woman with natural hair, hoop earrings and a gold crown"></div>
    </section>
  </main>
</body>
</html>
```